Never Stay Meek needs a book cover design

I need a book cover design for the following title:
Never Stay Meek-Grow a Bold Captain
Family methods from Cradle to Silver Years
by Dr. Walter P. Ondrak
I am interviewing a number of strong Canadian Leaders-specifically with regard to their experience of being parented. The book is a reaction today of parents having no backbone, no will nor ability to discipline their children. Many parents want to make a change but don't know how to.
Updates
Title should be "Never Stay Meek-Grow a Bold Captain" the rest is correct Added Wednesday, November 11, 2015
Here is an example of what we would need on the back cover in text only.
What does it take to raise a strong leader? Psychologist Dr. Walter P. Ondrak provides you with 6 must do strategies based on his 26 years of clinical experience and the interview of 6 strong leaders for this book. Strategies that you can start using today to insure your child’s success.
Target Market(s)
parents and grandparents
Requirements
Must have
- a way to communicate strength in parenting

```html
<!DOCTYPE html>
<html lang="en">
<head>
<meta charset="utf-8">
<title>Never Stay Meek – Grow a Bold Captain</title>
<link rel="stylesheet" href="https://fonts.googleapis.com/css2?family=Bebas+Neue&family=Montserrat:wght@800&family=Source+Sans+3:wght@400&display=swap">
<style>
  :root {
    --wall: #cdd6da;
    --wall-light: #dbe2e5;
    --wall-shade: #bdc8cd;
    --title-blue: #2a8ccd;
    --ink-dark: #1f2326;
    --body-ink: #1c1c1c;
    --author-white: #ffffff;
    --spine-author: #ffffff;
    --glow-warm: #fff3cf;
    --glow-mid: #f0d9a6;
  }
  html, body {
    margin: 0;
    padding: 0;
    overflow: hidden;
    background: var(--wall);
  }
  .cover-spread {
    position: relative;
    width: 1200px;
    height: 860px;
    overflow: hidden;
    background:
      radial-gradient(ellipse at 30% 40%, var(--wall-light) 0%, transparent 60%),
      radial-gradient(ellipse at 80% 20%, var(--wall-light) 0%, transparent 55%),
      linear-gradient(160deg, var(--wall-light) 0%, var(--wall) 50%, var(--wall-shade) 100%);
  }

  /* Back cover */
  .back-blurb {
    position: absolute;
    left: 36px;
    top: 200px;
    width: 504px;
    margin: 0;
    font-family: "Source Sans 3", sans-serif;
    font-size: 22px;
    line-height: 31.5px;
    color: var(--body-ink);
    text-align: justify;
  }

  /* Spine */
  .spine-title,
  .spine-author {
    position: absolute;
    writing-mode: vertical-rl;
    white-space: nowrap;
  }
  .spine-title {
    left: 585px;
    top: 43px;
    height: 502px;
    font-family: "Bebas Neue", sans-serif;
    font-size: 33px;
    line-height: 34px;
    color: var(--ink-dark);
    text-align: center;
    letter-spacing: 0.5px;
  }
  .spine-author {
    left: 590px;
    top: 572px;
    height: 270px;
    font-family: "Montserrat", sans-serif;
    font-weight: 800;
    font-size: 18px;
    line-height: 26px;
    color: var(--spine-author);
    text-align: center;
    letter-spacing: 0.5px;
    text-shadow: 0 0 3px rgba(60, 75, 82, 0.45);
  }

  /* Front cover */
  .front-title {
    position: absolute;
    left: 640px;
    top: 62px;
    width: 545px;
    margin: 0;
    font-family: "Bebas Neue", sans-serif;
    font-weight: 400;
    color: var(--title-blue);
    text-align: center;
  }
  .front-title .line { display: block; }
  .front-title .line-lead { font-size: 76px; line-height: 68px; }
  .front-title .line-big { font-size: 104px; line-height: 88px; }

  .front-subtitle {
    position: absolute;
    left: 640px;
    top: 304px;
    width: 545px;
    margin: 0;
    font-family: "Bebas Neue", sans-serif;
    font-size: 27px;
    line-height: 28px;
    letter-spacing: 3px;
    color: var(--ink-dark);
    text-align: center;
  }
  .front-subtitle .line { display: block; }

  .hero-photo {
    position: absolute;
    left: 720px;
    top: 438px;
    width: 380px;
    height: 422px;
    background:
      radial-gradient(ellipse at 52% 45%, var(--glow-warm) 0%, var(--glow-mid) 28%, rgba(205,214,218,0) 68%);
  }

  .front-author {
    position: absolute;
    left: 640px;
    top: 795px;
    width: 545px;
    margin: 0;
    font-family: "Montserrat", sans-serif;
    font-weight: 800;
    font-size: 30px;
    line-height: 40px;
    letter-spacing: 2px;
    color: var(--author-white);
    text-align: center;
    white-space: nowrap;
  }
</style>
</head>
<body>
  <main class="cover-spread">
    <section class="back-cover">
      <p class="back-blurb">What does it take to raise a strong leader? Psychologist Dr. Walter P. Ondrak provides you with 6 must do strategies based on his 26 years of clinical experience and the interview of 6 strong leaders for this book. Strategies that you can start using today to insure your child’s success.</p>
    </section>

    <section class="spine">
      <div class="spine-title">NEVER STAY MEEK GROW A BOLD CAPTAIN</div>
      <div class="spine-author">DR. WALTER P. ONDRAK</div>
    </section>

    <section class="front-cover">
      <h1 class="front-title">
        <span class="line line-lead">NEVER STAY MEEK</span>
        <span class="line line-lead">GROW A</span>
        <span class="line line-big">BOLD CAPTAIN</span>
      </h1>
      <p class="front-subtitle">
        <span class="line">FAMILY METHODS FROM CRADLE</span>
        <span class="line">TO SILVER YEARS</span>
      </p>
      <div class="hero-photo" role="img" aria-label="Photo of a young child seen from behind, raising both fists in a strong pose, backlit by warm sunlight"></div>
      <p class="front-author">DR. WALTER P. ONDRAK</p>
    </section>
  </main>
</body>
</html>
```